Business card for a "family office" company

Please provide professional looking business card designs, incorporating the attached logo and below details. Harrowmere Holdings Pty Ltd is a family office / financial investment company. We are looking for a modern, professional and contemporary card design.

Industry/Entity Type

Finance

Contact Information for Business Card

Name: Dean Mollick
Title: Director
Company: Harrowmere Holdings Pty Ltd
Email: harrowdean@quillnet.example
Mobile: 0462 735 418
Address: 4/312 Barnaby Parade, Marrowby WA 6099, Australia

Requirements
Must have
• All details above and the logo. logo only on back side. incorporate colours of logo
Nice to have
• up to you
Should not have
• ?

```html
<!DOCTYPE html>
<html lang="en">
<head>
<meta charset="utf-8">
<title>Harrowmere Holdings – Business Card</title>
<link rel="stylesheet" href="https://fonts.googleapis.com/css2?family=Roboto:wght@400;500;700&display=swap">
<style>
  :root {
    --backdrop: #e3e3e3;
    --paper: #f4f4f4;
    --navy: #1c1b56;
    --accent-blue: #2b3597;
    --body-grey: #555555;
    --white: #ffffff;
  }
  * { margin: 0; padding: 0; box-sizing: border-box; }
  html, body {
    width: 1200px; height: 960px; overflow: hidden;
    background: var(--backdrop);
    font-family: "Roboto", Arial, sans-serif;
  }
  .canvas { position: relative; width: 1200px; height: 960px; }

  .card { position: absolute; width: 601px; height: 342px; }
  .card-front { left: 314px; top: 113px; background: var(--paper); }
  .card-back { left: 311px; top: 472px; background: var(--navy); }

  .name-marker {
    position: absolute; left: 0; top: 50px;
    width: 12px; height: 39px; background: var(--navy);
  }
  .holder { position: absolute; left: 44px; top: 48px; }
  .holder-name {
    font-weight: 700; font-size: 20px; color: var(--navy);
    line-height: 24px;
  }
  .holder-title {
    font-weight: 500; font-size: 15px; color: var(--accent-blue);
    line-height: 20px;
  }

  .company-details {
    position: absolute; left: 44px; top: 183px;
    font-style: normal;
    font-size: 14px; line-height: 18.5px; color: var(--body-grey);
  }
  .company-name { font-weight: 500; }

  .contact-list {
    position: absolute; left: 44px; top: 249px;
    list-style: none; font-size: 14px; color: var(--body-grey);
  }
  .contact-list li { display: flex; align-items: center; height: 19.5px; }
  .contact-icon { width: 13px; height: 13px; margin-right: 9px; fill: var(--navy); flex: none; }

  .brand-name {
    position: absolute; font-weight: 500; text-align: center;
    letter-spacing: 3px; text-transform: uppercase; line-height: 1.25;
  }
  .card-front .brand-name {
    left: 300px; width: 290px; top: 250px;
    font-size: 19px; color: var(--navy);
  }
  .card-back .brand-name {
    left: 0; width: 100%; top: 158px;
    font-size: 26px; color: var(--white);
  }
  .back-web {
    position: absolute; left: 0; width: 100%; top: 296px;
    text-align: center; font-size: 14px; letter-spacing: 4px; color: var(--white);
  }
</style>
</head>
<body>
<main class="canvas">

  <section class="card card-front" aria-label="Card front">
    <div class="name-marker"></div>
    <div class="holder">
      <p class="holder-name">DEAN MOLLICK</p>
      <p class="holder-title">DIRECTOR</p>
    </div>

    <address class="company-details">
      <p class="company-name">Harrowmere Holdings Pty Ltd</p>
      <p>4/312 Barnaby Parade</p>
      <p>Marrowby WA 6099, Australia</p>
    </address>

    <ul class="contact-list">
      <li>
        <svg class="contact-icon" viewBox="0 0 13 13" aria-hidden="true"><path d="M3 0h7a1 1 0 0 1 1 1v11a1 1 0 0 1-1 1H3a1 1 0 0 1-1-1V1a1 1 0 0 1 1-1zm.6 1.5v8.5h5.8V1.5zM6.5 10.6a.8.8 0 1 0 0 1.6.8.8 0 0 0 0-1.6z"/></svg>
        0462 735 418
      </li>
      <li>
        <svg class="contact-icon" viewBox="0 0 13 13" aria-hidden="true"><path d="M0 3h13v7.5H0zm1.4 1.2 5.1 3.6 5.1-3.6z" fill-rule="evenodd"/></svg>
        harrowdean@quillnet.example
      </li>
      <li>
        <svg class="contact-icon" viewBox="0 0 13 13" aria-hidden="true"><path d="M6.5 0a6.5 6.5 0 1 0 0 13 6.5 6.5 0 0 0 0-13zm-1 2.2c.9.5 1.3 1.4.6 2.1-.6.6-1.8.3-1.8 1.3 0 .9 1.5.8 1.7 1.8.2.9-.6 1.7-.4 3.1A4.6 4.6 0 0 1 5.5 2.2zm3 1c.9.7.6 1.7 1.5 2 .6.2 1.1 0 1.2.5a4.6 4.6 0 0 1-2.4 4.9c-.4-.9.4-1.7-.3-2.5-.6-.6-1.6-.5-1.6-1.5 0-1.3 1.8-1.1 1.6-3.4z"/></svg>
        harrowmereholdings.example
      </li>
    </ul>

    <p class="brand-name">Harrowmere<br>Holdings</p>
  </section>

  <section class="card card-back" aria-label="Card back">
    <p class="brand-name">Harrowmere<br>Holdings</p>
    <p class="back-web">www.harrowmereholdings.example</p>
  </section>

</main>
</body>
</html>
```